Banner Design needed for Campus Recruitment Purpose!

Both Vortek5 and Harlow Quest & Associates is partner firms while Vortek5 is a career and talent management specialist, Harlow Quest & Associates focused on providing a premium executive search and recruitment services.

Banner designs are meant for our upcoming campus career fair exhibition and we requires a total of 3 banner designs that gives off a professional and mature vibes.
• 2 vertical banners design (approximately 61cm by 198cm)
• 1 expandable exhibition display banner design as the backdrop of our booth (approximately 230 cm by 230cm)
P.S. I have uploaded a sample of how the expandable exhibition display stand is like so you can have an idea of how big it is.

Purpose of exhibition is to:
• Introduce and recruit associates for Harlow Quest & Associates
• Introduce and promote PeakStride, a career consulting program under Vortek5, to individuals with the aim of imparting knowledge to enhance their ability and chances to get a job!

1. First Vertical Banner Design for Harlow Quest & Associates has to include:
• Harlow Quest & Associates Logo
• Harlow Quest & Associates Slogan: The preferred firm for premium executive search and recruitment services globally
• Relevant graphics relating to executive search services
• 5 bullet points of our services which is,
o Executive Search & Recruitment
o Contract Placement
o Onboarding Coaching
o Executive Coaching
o Leadership Assessment
• Background color of the banner has to be the same as the logo’s background which is the charcoal grey
• Color theme used in the banner has to match the Harlow’s logo colors

2. Second Vertical Banner Design for Vortek5’s PeakStride has to include:
• Vortek5’s Logo
• Vortek5’s Slogan: Career & Talent Management Specialists
• Relevant graphics
• Suitable wording design for the word, “PeakStride”
• Do create an area to include brief information of the program

3. Design for expandable exhibition display banner has to include:
• Logos of both Vortek5 and Harlow Quest & Associates
• Right side: Vortek5, Left side: Harlow Quest & Associates
• Require your help to blend and design the background whereby it can complement both logos with aim of making them into one picture

Target Market(s)

Individuals of age 25 - 40

Industry/Entity Type

Management

Font styles to use
Serif
Sans Serif

Requirements
Should not have
• The banners should not look too casual or playful.

```html
<!DOCTYPE html>
<html lang="en">
<head>
<meta charset="utf-8">
<title>Harlow Quest &amp; Associates — Vertical Banner</title>
<link rel="stylesheet" href="https://fonts.googleapis.com/css2?family=Cinzel:wght@500&family=Nunito:wght@400;500&display=swap">
<style>
  :root {
    --charcoal: #232323;
    --charcoal-light: #2c2c2c;
    --gold: #b8995c;
    --gold-soft: #9c7f52;
    --sage: #7f968c;
    --clay: #c1775c;
    --sand: #c9b48c;
    --white: #ffffff;
  }
  * { margin: 0; padding: 0; box-sizing: border-box; }
  html, body {
    width: 1200px;
    height: 3896px;
    overflow: hidden;
    background: var(--charcoal);
  }
  .banner {
    position: relative;
    width: 1200px;
    height: 3896px;
    overflow: hidden;
    background:
      radial-gradient(ellipse 700px 500px at 15% 40%, var(--charcoal-light) 0%, rgba(44,44,44,0) 100%),
      radial-gradient(ellipse 600px 500px at 90% 22%, var(--charcoal-light) 0%, rgba(44,44,44,0) 100%),
      radial-gradient(ellipse 700px 500px at 80% 65%, var(--charcoal-light) 0%, rgba(44,44,44,0) 100%),
      var(--charcoal);
  }
  .brand {
    position: absolute;
    left: 100px;
    top: 180px;
    display: flex;
    align-items: center;
    gap: 44px;
  }
  .brand-mark {
    width: 200px;
    height: 200px;
    border-radius: 50%;
    background: var(--gold);
    flex: none;
  }
  .brand-name {
    font-family: "Cinzel", serif;
    font-weight: 500;
    color: var(--gold);
    font-size: 96px;
    line-height: 1.05;
    text-transform: uppercase;
  }
  .brand-name small {
    display: block;
    font-size: 66px;
    letter-spacing: 1px;
  }
  .slogan {
    position: absolute;
    top: 650px;
    left: 0;
    width: 100%;
    text-align: center;
    font-family: "Nunito", sans-serif;
    font-weight: 500;
    color: var(--white);
    font-size: 66px;
    line-height: 108px;
  }
  .hero-graphic {
    position: absolute;
    left: 180px;
    top: 1180px;
    width: 840px;
    height: 820px;
    background:
      radial-gradient(ellipse 230px 400px at 30% 55%, var(--gold-soft) 0%, var(--gold-soft) 55%, rgba(156,127,82,0) 100%),
      radial-gradient(ellipse 230px 400px at 70% 55%, var(--sage) 0%, var(--sage) 55%, rgba(127,150,140,0) 100%);
  }
  .services {
    position: absolute;
    left: 104px;
    top: 2250px;
    list-style: none;
    font-family: "Nunito", sans-serif;
    font-weight: 500;
    color: var(--white);
    font-size: 64px;
    line-height: 110px;
  }
  .services li {
    display: flex;
    align-items: center;
  }
  .services li::before {
    content: "";
    width: 18px;
    height: 18px;
    border-radius: 50%;
    background: var(--gold);
    margin-right: 22px;
    flex: none;
  }
  .crowd-graphic {
    position: absolute;
    left: 0;
    bottom: 0;
    width: 1200px;
    height: 820px;
    background:
      radial-gradient(ellipse 200px 520px at 8% 100%, var(--clay) 0%, var(--clay) 50%, rgba(193,119,92,0) 100%),
      radial-gradient(ellipse 220px 600px at 28% 100%, var(--sand) 0%, var(--sand) 50%, rgba(201,180,140,0) 100%),
      radial-gradient(ellipse 230px 820px at 50% 100%, var(--sand) 0%, var(--sand) 55%, rgba(201,180,140,0) 100%),
      radial-gradient(ellipse 200px 560px at 77% 100%, var(--clay) 0%, var(--clay) 50%, rgba(193,119,92,0) 100%),
      radial-gradient(ellipse 180px 420px at 96% 100%, var(--gold) 0%, var(--gold) 50%, rgba(184,153,92,0) 100%);
  }
</style>
</head>
<body>
  <main class="banner">
    <header class="brand">
      <span class="brand-mark" aria-hidden="true"></span>
      <div class="brand-name">Harlow Quest<small>&amp; Associates</small></div>
    </header>

    <p class="slogan">The preferred firm for<br>premium executive search and<br>recruitment services globally</p>

    <div class="hero-graphic" role="img" aria-label="Illustration of two business people in suits, one tan and one sage green, giving each other a high five"></div>

    <ul class="services">
      <li>Executive Search &amp; Recruitment</li>
      <li>Contract Placement</li>
      <li>Onboarding Coaching</li>
      <li>Executive Coaching</li>
      <li>Leadership Assessment</li>
    </ul>

    <div class="crowd-graphic" role="img" aria-label="Illustration of many raised hands in tan, sand and terracotta tones rising from the bottom edge"></div>
  </main>
</body>
</html>
```